Exciting new vermouth brand needs a brilliant label!

We need a label design for an exciting new premium Italian Vermouth brand called Lunavera Vermouth.

Lunavera Vermouth is based on a recipe that has been handed down for four generations and is made in the traditional way in the Piedmonte region of Northern Italy.

Lunavera, which means 'heavenly' in Italian has been designed to elevate classic cocktails such as the Negroni, Americano and Manhattan with a base of Italian wine blended with botanicals such as wormwood, orange peel, rhubarb and cinchona. It has a delicately balanced bittersweet profile with hints of vanilla and citrus.

Its competitors include brands such as Vecchia Ricetta, Brunetti and Fabrizzi (see the uploaded brief for more examples).

The label is for a 50cl dark bottle (please refer to the uploaded brief) and should be based on maximum dimensions of 70mm (width) x 110mm (height). There is no limit to embellishments such as foil printing, embossing or any other premium finishes. The label does not necessarily need to be rectangular.

Feedback will be given quickly and constructively after submissions to ensure that the process is as fair and useful as possible for everyone.

Target Market(s)

25-45 year old Europeans, 50:50 female:male

Industry/Entity Type

Wine / Spirits / Vermouth

Requirements
Must have
• Fantastic design that is distinct from competitors, a premium feel and great lettering.
Should not have
• Generic images or patterns that do not relate to the brand (Lunavera) or the product

```html
<!DOCTYPE html>
<html lang="en">
<head>
<meta charset="utf-8">
<title>Lunavera Vermouth – Label</title>
<link rel="stylesheet" href="https://fonts.googleapis.com/css2?family=Oswald:wght@400;700&family=Montserrat:wght@400&family=Kaushan+Script&family=Open+Sans:wght@400&display=swap">
<style>
  :root {
    --bg: #ffffff;
    --gold-light: #f7d84a;
    --gold-mid: #e2b318;
    --gold-deep: #a86b06;
    --brown-ink: #4a2204;
    --panel-dark: #151515;
    --panel-mid: #262626;
    --text-gold: #e9bb2a;
  }
  html, body {
    margin: 0;
    padding: 0;
    width: 1200px;
    height: 1200px;
    overflow: hidden;
    background: var(--bg);
  }
  .label-canvas {
    display: block;
    width: 1200px;
    height: 1200px;
  }
  .eyebrow {
    font-family: "Oswald", sans-serif;
    font-weight: 400;
    font-size: 26px;
    letter-spacing: 6px;
    fill: var(--brown-ink);
  }
  .headline {
    font-family: "Oswald", sans-serif;
    font-weight: 700;
    font-size: 62px;
    fill: var(--brown-ink);
  }
  .brand-name {
    font-family: "Montserrat", sans-serif;
    font-weight: 400;
    font-size: 46px;
    letter-spacing: 3px;
    fill: var(--text-gold);
  }
  .product-type {
    font-family: "Kaushan Script", cursive;
    font-size: 68px;
    fill: var(--text-gold);
  }
  .body-copy {
    font-family: "Open Sans", sans-serif;
    font-size: 9.6px;
    fill: var(--text-gold);
  }
  .ribbon-text {
    font-family: "Oswald", sans-serif;
    font-weight: 700;
    font-size: 62px;
    fill: var(--brown-ink);
  }
  .star { fill: var(--brown-ink); }
</style>
</head>
<body>
<svg class="label-canvas" viewBox="0 0 1200 1200" xmlns="http://www.w3.org/2000/svg">
  <defs>
    <linearGradient id="gold-h" x1="0" y1="0" x2="1" y2="0">
      <stop offset="0" stop-color="var(--gold-deep)"/>
      <stop offset="0.12" stop-color="var(--gold-mid)"/>
      <stop offset="0.5" stop-color="var(--gold-light)"/>
      <stop offset="0.88" stop-color="var(--gold-mid)"/>
      <stop offset="1" stop-color="var(--gold-deep)"/>
    </linearGradient>
    <linearGradient id="gold-v" x1="0" y1="0" x2="0" y2="1">
      <stop offset="0" stop-color="var(--gold-mid)"/>
      <stop offset="0.5" stop-color="var(--gold-light)"/>
      <stop offset="1" stop-color="var(--gold-deep)"/>
    </linearGradient>
    <linearGradient id="panel-fill" x1="0" y1="0" x2="1" y2="0">
      <stop offset="0" stop-color="var(--panel-dark)"/>
      <stop offset="0.5" stop-color="var(--panel-mid)"/>
      <stop offset="1" stop-color="var(--panel-dark)"/>
    </linearGradient>
    <radialGradient id="ornament-fill" cx="0.5" cy="0.5" r="0.5">
      <stop offset="0" stop-color="var(--gold-mid)" stop-opacity="0.55"/>
      <stop offset="1" stop-color="var(--gold-mid)" stop-opacity="0"/>
    </radialGradient>
    <symbol id="star" viewBox="-10 -10 20 20">
      <polygon points="0,-10 2.9,-3.1 9.5,-3.1 4.2,1.3 5.9,8.1 0,4.2 -5.9,8.1 -4.2,1.3 -9.5,-3.1 -2.9,-3.1"/>
    </symbol>
  </defs>

  <!-- Label body -->
  <g class="label">
    <rect class="label-sidebars" x="430" y="197" width="340" height="801" fill="url(#gold-h)"/>
    <path class="label-top-cap" d="M450 310 L450 200 Q450 100 600 100 Q750 100 750 200 L750 310 Z" fill="url(#gold-v)"/>
    <path class="label-top-rule" d="M462 310 L462 204 Q462 116 600 116 Q738 116 738 204 L738 310" fill="none" stroke="var(--gold-deep)" stroke-width="2"/>
    <path class="label-bottom-cap" d="M450 880 L450 994 Q450 1094 600 1094 Q750 1094 750 994 L750 880 Z" fill="url(#gold-v)"/>
    <path class="label-bottom-rule" d="M462 880 L462 990 Q462 1078 600 1078 Q738 1078 738 990 L738 880" fill="none" stroke="var(--gold-deep)" stroke-width="2"/>

    <g class="stars-top">
      <use href="#star" class="star" x="540" y="163" width="22" height="22"/>
      <use href="#star" class="star" x="568" y="150" width="22" height="22"/>
      <use href="#star" class="star" x="589" y="145" width="22" height="22"/>
      <use href="#star" class="star" x="610" y="150" width="22" height="22"/>
      <use href="#star" class="star" x="638" y="163" width="22" height="22"/>
    </g>

    <text class="eyebrow" x="600" y="218" text-anchor="middle">- PREMIUM -</text>
    <text class="headline" x="600" y="286" text-anchor="middle" textLength="182" lengthAdjust="spacingAndGlyphs">PRODUCT</text>

    <rect class="label-panel" x="454" y="304" width="296" height="500" fill="url(#panel-fill)"/>

    <g class="ornament-top" role="img" aria-label="Gold scroll flourish above the brand name">
      <rect x="510" y="312" width="180" height="82" fill="url(#ornament-fill)"/>
    </g>
    <line class="rule" x1="488" y1="400" x2="712" y2="400" stroke="var(--gold-mid)" stroke-width="2"/>

    <text class="brand-name" x="600" y="450" text-anchor="middle">Lunavera</text>
    <text class="product-type" x="600" y="530" text-anchor="middle">Vermouth</text>

    <line class="rule" x1="488" y1="566" x2="712" y2="566" stroke="var(--gold-mid)" stroke-width="2"/>
    <g class="ornament-bottom" role="img" aria-label="Gold scroll flourish below the product name">
      <rect x="510" y="572" width="180" height="74" fill="url(#ornament-fill)"/>
    </g>

    <text class="body-copy" x="468" y="668">
      <tspan x="468" dy="0">A new sweet vermouth for the home cocktail maker,</tspan>
      <tspan x="468" dy="11.5">made to lift every glass. Italian wine, gently fortified,</tspan>
      <tspan x="468" dy="11.5">sweetened and steeped with a blend of aromatic, bitter,</tspan>
      <tspan x="468" dy="11.5">sweet and citrus botanicals (wormwood, vanilla,</tspan>
      <tspan x="468" dy="11.5">rhubarb root, cinnamon, clove, orange peel, orris,</tspan>
      <tspan x="468" dy="11.5">cinchona). Enjoy it neat over ice or stirred into a</tspan>
      <tspan x="468" dy="11.5">Negroni, Americano or Manhattan.</tspan>
    </text>

    <g class="stars-bottom">
      <use href="#star" class="star" x="540" y="1018" width="22" height="22"/>
      <use href="#star" class="star" x="568" y="1030" width="22" height="22"/>
      <use href="#star" class="star" x="589" y="1034" width="22" height="22"/>
      <use href="#star" class="star" x="610" y="1030" width="22" height="22"/>
      <use href="#star" class="star" x="638" y="1018" width="22" height="22"/>
    </g>
  </g>

  <!-- Offer ribbon -->
  <g class="offer-ribbon">
    <polygon class="ribbon-tail-left" points="354,858 420,845 451,958 354,971 391,918" fill="url(#gold-v)"/>
    <polygon class="ribbon-tail-right" points="781,798 847,789 813,858 847,905 781,916" fill="url(#gold-v)"/>
    <polygon class="ribbon-fold-left" points="420,925 485,916 485,958 451,958" fill="#6d4a05"/>
    <polygon class="ribbon-fold-right" points="781,872 720,880 720,905 781,916" fill="#6d4a05"/>
    <polygon class="ribbon-band" points="420,812 781,761 781,872 420,925" fill="url(#gold-h)"/>
    <line x1="420" y1="822" x2="781" y2="771" stroke="var(--gold-deep)" stroke-width="1.5"/>
    <line x1="420" y1="915" x2="781" y2="862" stroke="var(--gold-deep)" stroke-width="1.5"/>
    <text class="ribbon-text" x="600" y="866" text-anchor="middle" transform="rotate(-8 600 845)" textLength="330" lengthAdjust="spacingAndGlyphs">SPECIAL OFFER</text>
  </g>
</svg>
</body>
</html>
```